Venture capital website it shall be called Talvo Ventures

Venture capital Name is : Talvo Ventures

i have already regesieted a website and comunicate the details with you when i choose a design.

i need a simple website design for a newly established venture capital. i would like something similar to the websites listed down:

http://www.quillmarsh.com/

http://www.derobrightventures.com/

https://kplorin.com/

http://www.vintelhold.com/

i like vintel hold the most

Target Market(s)

entrepreneur - startups

Industry/Entity Type

Venture Capital

Number of Pages Required

4 page

Font styles to use
Serif
Sans Serif

Colors
ffc214
fece3e

Requirements
Must have
• the following sections:
• Philosophy (about talvo Ventures)
• Team
• Knowledge
• address - contact
Nice to have
• http://www.quillmarsh.com/
• http://www.derobrightventures.com/
• https://kplorin.com/
• http://www.vintelhold.com/

```html
<!DOCTYPE html>
<html lang="en">
<head>
<meta charset="utf-8">
<title>Talvo Ventures — Team</title>
<link rel="stylesheet" href="https://fonts.googleapis.com/css2?family=Cinzel:wght@700&family=Roboto:wght@300&display=swap">
<style>
  :root {
    --brand-yellow: #ffc214;
    --brand-yellow-soft: #fece3e;
    --ink: #111111;
    --body-text: #222222;
    --paper: #ffffff;
    --nav-text: #ffffff;
    --scroll-button: #b89b30;
    --photo-tone-a: #e9e4dc;
    --photo-tone-b: #cfc6b8;
  }
  * { box-sizing: border-box; margin: 0; padding: 0; }
  html, body {
    width: 1148px;
    height: 1200px;
    overflow: hidden;
    background: var(--paper);
  }
  .page {
    position: relative;
    width: 1148px;
    height: 1200px;
    overflow: hidden;
  }
  .site-header {
    position: absolute;
    left: 0; top: 0;
    width: 100%;
    height: 168px;
    background: var(--brand-yellow);
  }
  .main-nav a {
    position: absolute;
    top: 74px;
    font-family: "Cinzel", Georgia, serif;
    font-weight: 700;
    font-size: 30px;
    line-height: 1;
    letter-spacing: 0.5px;
    color: var(--nav-text);
    text-decoration: none;
    padding-bottom: 8px;
    border-bottom: 3px solid var(--ink);
  }
  .main-nav a.is-current { color: var(--ink); }
  .nav-philosophy { left: 103px; }
  .nav-team { left: 391px; }
  .nav-knowledge { left: 589px; }
  .nav-contact { left: 877px; top: 78px !important; }

  .team-member { position: absolute; left: 0; width: 100%; }
  .member-one { top: 228px; }
  .member-two { top: 793px; }

  .member-portrait {
    position: absolute;
    left: 102px;
    top: 0;
    width: 244px;
    height: 244px;
    border-radius: 50%;
    border: 5px solid var(--brand-yellow);
    background: linear-gradient(160deg, var(--photo-tone-a), var(--photo-tone-b));
  }
  .member-bio {
    position: absolute;
    left: 434px;
    width: 628px;
    font-family: "Roboto", Arial, sans-serif;
    font-weight: 300;
    font-size: 22px;
    color: var(--body-text);
    text-align: center;
  }
  .member-one .member-bio { top: 8px; line-height: 40px; }
  .member-two .member-bio { top: 0; line-height: 42px; }

  .scroll-control {
    position: absolute;
    left: 21px;
    top: 1105px;
    width: 80px;
    height: 80px;
  }
</style>
</head>
<body>
<div class="page">
  <header class="site-header">
    <nav class="main-nav">
      <a class="nav-philosophy" href="#philosophy">Philosophy</a>
      <a class="nav-team is-current" href="#team">Team</a>
      <a class="nav-knowledge" href="#knowledge">Knowledge</a>
      <a class="nav-contact" href="#contact">Contact</a>
    </nav>
  </header>

  <section class="team-member member-one">
    <div class="member-portrait" role="img" aria-label="Portrait photo of Faisal Al Darmi"></div>
    <p class="member-bio">Faisal Al Darmi holds a BA degree in Mass Media from Qaryan University. Al Darmi is Founder &amp; General Manager of Nawrah, the leading Social Media Agency in Kuwait &amp; the GCC. Nawrah was the first agency of its sort in the region. It opted to divert marketing from its typical offline focus &amp; shifted the direction online, to Social Media. Through Faisal Al Darmi, vision and reach the company expanded from Kuwait to Saudi Arabia, and then Qatar.</p>
  </section>

  <section class="team-member member-two">
    <div class="member-portrait" role="img" aria-label="Portrait photo of Yousef Nabil Al-Haddar"></div>
    <p class="member-bio">Yousef Nabil Al-Haddar holds a BA degree in Finance from Qaryan University. He has vast knowledge and skills in areas such as merger and acquisition, business strategy, financial analysis, evaluating business opportunities, and evaluating companies in different sectors.</p>
  </section>

  <svg class="scroll-control" viewBox="0 0 80 80" aria-label="Scroll navigation">
    <circle cx="40" cy="40" r="40" fill="var(--scroll-button)"/>
    <polygon points="40,12 51,24 29,24" fill="#ffffff"/>
    <polygon points="40,68 51,56 29,56" fill="#ffffff"/>
    <polygon points="14,40 24,30 24,50" fill="#ffffff"/>
  </svg>
</div>
</body>
</html>
```